hotel amenities supply company needs design for bottles and accessories

we need to design four 30ml amenity tubes branded "ORVENTA" , shampoo, shower gel, conditioner and body lotion. the bottle has to be somewhat clear to be able to see the liquid inside. its basically designing the complete identity for "orventa". attached are some examples. also the accessory boxes should match the design eg, shaving kit,vanity kit, toothbrush etc

Target Market(s)

hotels

Industry/Entity Type

Hotel

Font styles to use
Script

Requirements
Must have
• name "orventa " on bottles and product info
Should not have
• dark colors

```html
<!DOCTYPE html>
<html lang="en">
<head>
<meta charset="utf-8">
<title>Orventa Moisturizing Body Lotion – 30 ml Tube</title>
<link rel="stylesheet" href="https://fonts.googleapis.com/css2?family=Josefin+Sans:wght@400;600&display=swap">
<style>
  :root {
    --backdrop: #7368cc;
    --tube-top: #d9d5f6;
    --tube-bottom: #c3bcef;
    --crimp: #e4e0fa;
    --crimp-line: #cfc9f3;
    --pattern-light: rgba(255,255,255,0.35);
    --pattern-soft: rgba(200,194,238,0.4);
    --cap-light: #e6e3f3;
    --cap-mid: #b9b4cc;
    --cap-dark: #8f89a6;
    --ink: #2b2838;
  }
  * { margin: 0; padding: 0; box-sizing: border-box; }
  html, body { width: 1200px; height: 1029px; overflow: hidden; }
  body { background: var(--backdrop); position: relative; }

  .tube { position: absolute; left: 488px; top: 330px; width: 226px; height: 562px; }
  .tube-shape { position: absolute; inset: 0; }

  .label-art {
    position: absolute; left: 96px; top: 28px; width: 118px; height: 230px;
    background: radial-gradient(ellipse at 60% 40%, var(--pattern-light), var(--pattern-soft) 55%, transparent 80%);
    border-radius: 40px 10px 60px 20px;
  }

  .vertical { writing-mode: vertical-rl; transform: rotate(180deg); white-space: nowrap; position: absolute; }
  .brand-name {
    left: 46px; bottom: 160px;
    font-family: "Josefin Sans", sans-serif; font-weight: 400; font-size: 28px; letter-spacing: 10px;
    color: var(--ink); text-transform: uppercase;
  }
  .product-kicker {
    left: 109px; bottom: 160px;
    font-family: "Josefin Sans", sans-serif; font-size: 12px; letter-spacing: 0.3px;
    color: var(--ink); text-transform: uppercase;
  }
  .product-name {
    left: 120px; bottom: 160px;
    font-family: "Josefin Sans", sans-serif; font-weight: 600; font-size: 23px; letter-spacing: 1px;
    color: var(--ink); text-transform: uppercase;
  }
  .claim {
    left: 162px; bottom: 160px;
    font-family: "Josefin Sans", sans-serif; font-size: 16px; letter-spacing: 0.5px;
    color: var(--ink); text-transform: uppercase;
  }
  .claim-detail {
    left: 179px; bottom: 160px;
    font-family: "Josefin Sans", sans-serif; font-size: 6.5px;
    color: var(--ink); text-transform: uppercase;
  }
  .volume {
    position: absolute; left: 96px; top: 424px;
    font-family: "Josefin Sans", sans-serif; font-size: 13px; color: var(--ink);
  }
</style>
</head>
<body>
  <div class="tube">
    <svg class="tube-shape" width="226" height="562" viewBox="0 0 226 562">
      <defs>
        <linearGradient id="tubeBody" x1="0" y1="0" x2="0" y2="1">
          <stop offset="0" stop-color="var(--tube-top)"/>
          <stop offset="1" stop-color="var(--tube-bottom)"/>
        </linearGradient>
        <linearGradient id="capMetal" x1="0" y1="0" x2="1" y2="0">
          <stop offset="0" stop-color="var(--cap-dark)"/>
          <stop offset="0.35" stop-color="var(--cap-light)"/>
          <stop offset="0.7" stop-color="var(--cap-mid)"/>
          <stop offset="1" stop-color="var(--cap-dark)"/>
        </linearGradient>
      </defs>
      <path d="M0 24 L226 24 Q214 300 192 455 L34 455 Q12 300 0 24 Z" fill="url(#tubeBody)"/>
      <rect x="0" y="0" width="226" height="24" fill="var(--crimp)"/>
      <g stroke="var(--crimp-line)" stroke-width="1.5">
        <line x1="4" y1="4" x2="222" y2="4"/>
        <line x1="4" y1="20" x2="222" y2="20"/>
      </g>
      <rect x="34" y="455" width="158" height="107" rx="3" fill="url(#capMetal)"/>
      <rect x="34" y="480" width="158" height="4" fill="var(--cap-light)"/>
      <rect x="34" y="530" width="158" height="2" fill="var(--cap-dark)"/>
    </svg>

    <div class="label-art" role="img" aria-label="Abstract translucent branch pattern on the tube label"></div>

    <span class="brand-name vertical">Orventa</span>

    <span class="product-kicker vertical">Moisturizing</span>
    <span class="product-name vertical">Body Lotion</span>
    <span class="claim vertical">Long Lasting</span>
    <span class="claim-detail vertical">Keep your skin soft &amp; smooth</span>

    <span class="volume">30 ml</span>
  </div>
</body>
</html>
```